CREATIVE DESIGNERS NEEDED & Enhance Your Business Card Portfolio

Artistic, unique, professional real estate card needed - see attached documents "B-cards.pdf" for all details and examples.True Designers will see other projects of ours come online here. We like long-term relationships for creative designers. This business card will be used in two U.S. states and is central to our business and other future marketing.

Target Market(s)

Buyers and Sellers of real estate

Industry/Entity Type

Real Estate Agent

Contact Information for Business Card

See attached detailed brief

Other font styles liked:
• ADAM.CG PRO & NewsGoth BT

Requirements
Must have
• 2-sided, creative (non-traditional layout/design). Incorporate a cut-out (for texture, and make it fun! No boring templates for this card -
Nice to have
• See attached detailed brief
Should not have

```html
<!DOCTYPE html>
<html lang="en">
<head>
<meta charset="utf-8">
<title>Reed Harlow Group Real Estate – Business Card</title>
<link href="https://fonts.googleapis.com/css2?family=Montserrat:wght@400;500;600;700&family=PT+Serif:wght@400&display=swap" rel="stylesheet">
<style>
  :root{
    --backdrop:#2b2b2d;
    --card-white:#ffffff;
    --card-dark:#1d1d1f;
    --slate:#4a5563;
    --red:#c8302f;
    --red-soft:#b8413f;
    --text-light:#e9e9e9;
    --text-muted:#9a9a9a;
    --photo-dark:#1f2224;
    --photo-light:#8c9296;
  }
  *{margin:0;padding:0;box-sizing:border-box}
  html,body{width:1200px;height:900px;overflow:hidden;background:var(--backdrop)}
  .canvas{position:relative;width:1200px;height:900px;font-family:"Montserrat",Arial,sans-serif}

  .card{position:absolute;left:260px;width:680px;height:388px;overflow:hidden;box-shadow:0 12px 30px rgba(0,0,0,.45)}

  /* Front side */
  .card--front{top:50px;background:var(--card-white)}
  .front-mark{position:absolute;left:70px;top:74px;width:240px;height:240px;background:var(--slate)}
  .front-lockup{position:absolute;left:360px;top:140px;color:var(--slate);font-weight:600;line-height:1}
  .front-lockup .name{font-size:54px;letter-spacing:1px}
  .front-lockup .group{font-size:25px;letter-spacing:2px;margin-top:8px}
  .front-lockup .trade{font-size:18px;letter-spacing:9px;margin-top:12px}

  /* Back side */
  .card--back{top:462px;background:var(--card-dark)}
  .photo{position:absolute;right:0;top:0;width:290px;height:388px;
    background:linear-gradient(100deg,var(--photo-dark) 0%,var(--photo-light) 70%,#a9aeb1 100%)}
  .back-lockup{position:absolute;left:44px;top:40px;display:flex;align-items:center;gap:14px}
  .back-lockup .square{width:44px;height:44px;background:var(--text-light)}
  .back-lockup .words{color:var(--text-light);font-weight:600;line-height:1}
  .back-lockup .name{font-size:30px;letter-spacing:1px}
  .back-lockup .group{font-size:13px;letter-spacing:1.5px;margin-top:5px}
  .back-lockup .trade{font-size:10px;letter-spacing:5px;margin-top:5px}
  .region{position:absolute;left:102px;top:116px;font-family:"PT Serif",Georgia,serif;color:var(--text-muted);font-size:14px}
  .services{position:absolute;left:44px;top:160px;font-family:"PT Serif",Georgia,serif;color:var(--red-soft);font-size:14px}
  .agent{position:absolute;left:44px;top:212px;color:var(--text-light);font-size:20px}
  .agent strong{font-weight:700}
  .agent .title{font-size:15px;margin-left:6px}
  .rule{position:absolute;left:44px;top:248px;width:330px;height:2px;background:var(--red)}
  .phone{position:absolute;color:var(--red);font-size:15px;display:flex;align-items:center;gap:7px}
  .phone--office{left:44px;top:262px}
  .phone--mobile{left:216px;top:262px}
  .phone svg{width:15px;height:15px;fill:var(--red)}
  .badges{position:absolute;left:44px;top:316px;display:flex;gap:10px}
  .badge{height:36px;border:2px solid var(--text-muted);border-radius:3px}
  .badge--a{width:36px}
  .badge--b{width:62px}
</style>
</head>
<body>
<div class="canvas">

  <section class="card card--front" aria-label="Card front">
    <div class="front-mark"></div>
    <div class="front-lockup">
      <div class="name">REED</div>
      <div class="group">HARLOW GROUP</div>
      <div class="trade">REAL ESTATE</div>
    </div>
  </section>

  <section class="card card--back" aria-label="Card back">
    <div class="photo" role="img" aria-label="Black and white portrait photo of the agent"></div>

    <div class="back-lockup">
      <div class="square"></div>
      <div class="words">
        <div class="name">REED</div>
        <div class="group">HARLOW GROUP</div>
        <div class="trade">REAL ESTATE</div>
      </div>
    </div>
    <div class="region">San Diego &amp; Phoenix</div>
    <div class="services">Residential. Investment. Development</div>

    <div class="agent">Reed <strong>Harlow</strong><span class="title">Broker Associate &amp; Realtor</span></div>
    <div class="rule"></div>

    <div class="phone phone--office">
      <svg viewBox="0 0 24 24" aria-hidden="true"><path d="M3 8c0-2 4-4 9-4s9 2 9 4v2h-5V8H8v2H3z M6 11h12l2 9H4z"/></svg>
      (844) 555-0142
    </div>
    <div class="phone phone--mobile">
      (619) 555-0187
      <svg viewBox="0 0 24 24" aria-hidden="true"><path d="M7 2h10a1 1 0 0 1 1 1v18a1 1 0 0 1-1 1H7a1 1 0 0 1-1-1V3a1 1 0 0 1 1-1zm1 2v14h8V4z"/></svg>
    </div>

    <div class="badges">
      <div class="badge badge--a"></div>
      <div class="badge badge--b"></div>
    </div>
  </section>

</div>
</body>
</html>
```